Powerpoint Presentation Template

Kindly design a business class Powepoint Presentation template for our business use. Please stick to our company colours or even pictures as shown on our website and Logo

```html
<!DOCTYPE html>
<html lang="en">
<head>
<meta charset="utf-8">
<title>Presentation Template – Veramont Properties</title>
<link rel="stylesheet" href="https://fonts.googleapis.com/css2?family=Source+Sans+3:wght@400;600;700&display=swap">
<style>
  :root {
    --brand-red: #7d1f1b;
    --stripe-dark: #2a2a2a;
    --stripe-grey: #8a8a8a;
    --ink: #333333;
    --frame: #9a9a9a;
    --paper: #ffffff;
    --sketch-light: #f4ece9;
    --sketch-mid: #e3c9c2;
  }
  * { box-sizing: border-box; margin: 0; padding: 0; }
  html, body { width: 670px; height: 1200px; overflow: hidden; background: var(--paper); }
  body { position: relative; font-family: "Source Sans 3", Arial, sans-serif; color: var(--ink); }

  .slide {
    position: absolute; left: 28px; width: 614px; height: 345px;
    border: 1px solid var(--frame); background: var(--paper); overflow: hidden;
  }
  .slide--cover { top: 14px; }
  .slide--page { top: 408px; }
  .slide--pictures { top: 800px; }
  .slide svg.shapes { position: absolute; inset: 0; width: 100%; height: 100%; }

  .slide-label {
    position: absolute; right: 28px; font-size: 11px; font-weight: 700;
    letter-spacing: 0.02em; color: #222;
  }
  .slide-label--cover { top: 366px; }
  .slide-label--page { top: 760px; }
  .slide-label--pictures { top: 1152px; }

  .brand {
    position: absolute; right: 186px; top: 10px;
    display: flex; align-items: center; gap: 6px;
    color: var(--brand-red); font-size: 13px; font-weight: 600; line-height: 1;
    white-space: nowrap;
  }
  .brand__mark { width: 8px; height: 8px; background: var(--brand-red); }

  .cover-title {
    position: absolute; left: 30px; top: 146px; color: var(--paper);
    font-size: 38px; font-weight: 400; letter-spacing: 0.03em;
  }
  .cover-sketch {
    position: absolute; left: 0; right: 0; top: 215px; bottom: 0;
    background: linear-gradient(180deg, var(--sketch-mid) 0%, var(--sketch-light) 60%, var(--paper) 100%);
  }

  .page-title {
    position: absolute; left: 28px; top: 36px; color: var(--paper);
    font-size: 24px; font-weight: 400; letter-spacing: 0.03em;
  }
  .page-body {
    position: absolute; left: 28px; top: 100px; font-size: 12px; line-height: 1.42;
  }
  .slide--page .page-body { width: 370px; }
  .slide--pictures .page-body { width: 500px; }
  .bullets { list-style: none; margin-top: 10px; }
  .bullets li {
    position: relative; padding-left: 18px; margin-bottom: 8px; font-weight: 700;
  }
  .bullets li::before {
    content: ""; position: absolute; left: 3px; top: 6px;
    width: 5px; height: 5px; border-radius: 50%; background: var(--ink);
  }

  .photo-row { position: absolute; left: 45px; top: 222px; display: flex; gap: 36px; }
  .photo { width: 150px; height: 90px; }
  .photo--one { background: linear-gradient(160deg, #c9d4de 0%, #8e98a0 55%, #5d6167 100%); }
  .photo--two { background: linear-gradient(180deg, #7fa3c8 0%, #b8c3cc 50%, #6f6a63 100%); }
  .photo--three { background: linear-gradient(170deg, #8fb1d6 0%, #b7c4d0 55%, #7b8590 100%); }
</style>
</head>
<body>

  <section class="slide slide--cover">
    <div class="cover-sketch" role="img" aria-label="Architectural line sketch of a building under construction in red ink"></div>
    <svg class="shapes" viewBox="0 0 614 345" aria-hidden="true">
      <polygon points="0,128 590,128 614,150 614,215 0,215" fill="var(--brand-red)"/>
      <polygon points="440,0 478,0 614,124 614,160" fill="var(--stripe-dark)"/>
      <polygon points="488,0 498,0 614,106 614,116" fill="var(--stripe-grey)"/>
    </svg>
    <div class="brand"><span class="brand__mark"></span><span class="brand__name">Veramont Properties</span></div>
    <h1 class="cover-title">YOUR TITLE HERE</h1>
  </section>
  <div class="slide-label slide-label--cover">COVER / DIVIDER</div>

  <section class="slide slide--page">
    <svg class="shapes" viewBox="0 0 614 345" aria-hidden="true">
      <polygon points="0,28 470,28 520,75 0,75" fill="var(--brand-red)"/>
      <polygon points="440,0 474,0 614,128 614,160" fill="var(--stripe-dark)"/>
      <polygon points="484,0 494,0 614,110 614,120" fill="var(--stripe-grey)"/>
    </svg>
    <div class="brand"><span class="brand__mark"></span><span class="brand__name">Veramont Properties</span></div>
    <h2 class="page-title">YOUR TITLE HERE</h2>
    <div class="page-body">
      <p>Lorem ipsum dolor sit amet, consectetur adipiscing elit. Nulla efficitur varius euismod. Suspendisse potenti. Integer pharetra tellus eget elit cursus elementum. Phasellus at tempor enim. Vivamus et odio eu enim cursus aliquam. Nullam quis dui et eros tempus malesuada. Fusce a leo urna.</p>
      <ul class="bullets">
        <li>Sed sollicitudin erat id justo cursus pretium</li>
        <li>Vivamus feugiat tempus ante, vel scelerisque mauris aliquet efficitur</li>
        <li>Cras sed nulla ut odio aliquet sodales suscipit in dolor</li>
      </ul>
    </div>
  </section>
  <div class="slide-label slide-label--page">PAGE</div>

  <section class="slide slide--pictures">
    <svg class="shapes" viewBox="0 0 614 345" aria-hidden="true">
      <polygon points="0,28 470,28 520,75 0,75" fill="var(--brand-red)"/>
      <polygon points="440,0 474,0 614,128 614,160" fill="var(--stripe-dark)"/>
      <polygon points="484,0 494,0 614,110 614,120" fill="var(--stripe-grey)"/>
    </svg>
    <div class="brand"><span class="brand__mark"></span><span class="brand__name">Veramont Properties</span></div>
    <h2 class="page-title">YOUR TITLE HERE</h2>
    <div class="page-body">
      <p>Donec congue risus vitae sapien dictum, et dictum odio vehicula. Donec sed neque eget metus gravida porta. Mauris purus urna, sodales ut turpis eu, molestie fringilla quam. Phasellus porttitor maximus scelerisque. Nunc porta felis nec ultrices aliquet. Ut sit amet quam neque. Aliquam quis faucibus massa.</p>
    </div>
    <div class="photo-row">
      <div class="photo photo--one" role="img" aria-label="Photo of a modern office tower seen from below"></div>
      <div class="photo photo--two" role="img" aria-label="Photo of a building under construction with scaffolding"></div>
      <div class="photo photo--three" role="img" aria-label="Photo of city skyscrapers against a blue sky"></div>
    </div>
  </section>
  <div class="slide-label slide-label--pictures">PAGE WITH PICTURES</div>

</body>
</html>
```